Cordial Keys

We teach men how to be successful with women.

We will be putting an Vidhostly on the page.

We want to push men to take our 12 month learning program.

Open to ideas and layouts. The website will also be a landing page for our TV campaign.

Cordial keys is a company that will be marketing as an infomercial on late night television and via the internet. 

We will be selling a 12 month program for $997 (paid monthly). It will teach men how to get the woman of their dreams and how attraction is not a choice.
We have systematically developed a program for helping men attract women. 
We do have some competitors but they in the pickup commuinity (Hob Board, Greg Tolliver and Quillon Methods are all competitors.
Our website name is cordialkeys.com.au.
We will be having an vidhostly.com.au on our website to aid the process on making the sale.

The program will be an e-learning program that will be purchased over 12 months.

We also will be selling boot camps in which guys go for a week at a time and train to refine their skills.

Tv

```html
<!DOCTYPE html>
<html lang="en">
<head>
<meta charset="utf-8">
<title>Cordial Keys</title>
<link rel="stylesheet" href="https://fonts.googleapis.com/css2?family=Cabin:wght@400;500&family=Bevan&family=Anton&display=swap">
<style>
:root{
  --black:#000;
  --red:#d90000;
  --red-dark:#b80000;
  --blue:#1a7bc9;
  --page:#f6f6f6;
  --text:#5a5a5a;
  --rule:#e0e0e0;
  --quote-bg:#e5e5e5;
  --white:#fff;
}
*{margin:0;padding:0;box-sizing:border-box}
html,body{width:1200px;height:912px;overflow:hidden}
body{position:relative;background:var(--page);font-family:"Cabin",sans-serif;color:var(--text)}
.site-header{position:absolute;left:0;top:0;width:1200px;height:94px;background:var(--black)}
.brand{position:absolute;left:186px;top:26px;font-size:32px;font-weight:500;color:var(--red);letter-spacing:.5px;white-space:nowrap}
.main-nav{position:absolute;left:444px;top:36px;display:flex;align-items:center}
.main-nav a{color:var(--white);text-decoration:none;font-size:15.5px;padding:4px 7px;white-space:nowrap}
.main-nav a.current{background:linear-gradient(#fff,#e4e4e4);color:var(--red);border-radius:3px;padding:5px 8px;position:relative;margin-right:1px}
.main-nav a.current::after{content:"";position:absolute;left:50%;bottom:-6px;margin-left:-6px;border:6px solid transparent;border-top-color:#e4e4e4;border-bottom:0}
.edge{position:absolute;left:0;width:1200px;height:5px;display:block}
.edge-header{top:94px;z-index:2}
.edge-footer{top:825px}
.hero{position:absolute;left:0;top:94px;width:1200px;height:359px;
  background:linear-gradient(180deg,#2a2a5a 0%,#4a3f7a 35%,#8b5a86 62%,#e0805a 82%,#000 83%,#000 100%)}
.hero-title{position:absolute;left:217px;top:389px;width:520px;font-family:"Bevan",serif;font-weight:400;font-size:22px;line-height:32px;color:var(--white);white-space:nowrap}
.hero-cta{position:absolute;left:751px;top:375px;width:236px;height:58px;background:linear-gradient(#ee1a1a,var(--red-dark));border-radius:3px;
  font-family:"Anton",sans-serif;font-size:23px;color:var(--white);display:flex;align-items:center;justify-content:center;letter-spacing:.3px;white-space:nowrap}
.features{position:absolute;left:190px;top:481px;width:615px;display:flex}
.feature{width:205px;text-align:left;padding:0 8px;border-left:1px solid var(--rule)}
.feature:first-child{border-left:0}
.feature .icon{display:block;margin:0 auto 10px}
.feature h2{font-weight:400;font-size:17px;line-height:19px;color:var(--blue);text-align:center;margin-bottom:10px}
.feature p{font-size:12.5px;line-height:15.5px;padding-left:8px}
.stories-title{position:absolute;left:190px;top:679px;font-size:16px;font-weight:400;color:var(--red)}
.quote{position:absolute;left:189px;top:705px;width:615px;height:100px;background:var(--quote-bg);border:1px solid #d6d6d6;border-radius:3px;padding:14px 13px;font-size:12.5px;line-height:15.5px}
.quote cite{display:block;font-style:normal;color:#333;margin-top:9px}
.presenter{position:absolute;left:845px;top:560px;width:145px;height:270px;background:linear-gradient(180deg,#e8e4e2,#8a93a8 45%,#5d6682);border-radius:60px 60px 6px 6px}
.site-footer{position:absolute;left:0;top:830px;width:1200px;height:82px;background:var(--red)}
.footer-nav{position:absolute;left:188px;top:19px;display:flex;gap:15px}
.footer-nav a{color:var(--white);text-decoration:none;font-size:14.5px;white-space:nowrap}
.copyright{position:absolute;left:188px;top:42px;color:var(--white);font-size:12.5px;white-space:nowrap}
.social{position:absolute;left:880px;top:23px;display:flex;gap:6px}
.social span{width:37px;height:37px;background:#ececec;border-radius:2px;display:block}
</style>
</head>
<body>
<header class="site-header">
  <div class="brand">Cordial Keys</div>
  <nav class="main-nav">
    <a class="current" href="#">Home</a><a href="#">About us</a><a href="#">Bootcamp</a><a href="#">Learning Program</a><a href="#">Success Stories</a><a href="#">FAQ</a><a href="#">Contact us</a>
  </nav>
</header>
<svg class="edge edge-header" viewBox="0 0 1200 5" preserveAspectRatio="none">
  <defs><pattern id="teeth-down" width="8" height="5" patternUnits="userSpaceOnUse"><path d="M0 0 L4 5 L8 0Z" fill="#000"/></pattern></defs>
  <rect width="1200" height="5" fill="url(#teeth-down)"/>
</svg>

<section class="hero" role="img" aria-label="Silhouette of a lonely man sitting on a beach at sunset while a couple embraces under palm trees"></section>
<h1 class="hero-title">DON’T LET THIS HAPPEN TO YOU!</h1>
<div class="hero-cta">MAKE A CHANGE NOW!</div>

<section class="features">
  <article class="feature">
    <svg class="icon" width="52" height="52" viewBox="0 0 52 52"><circle cx="26" cy="26" r="25" fill="#222" stroke="#bbb"/><polygon points="20,15 37,26 20,37" fill="#ddd"/></svg>
    <h2>Make a Change<br>Now</h2>
    <p>Get the Woman of your Dream. Take our 12 month Learning Program. It’s Simple</p>
  </article>
  <article class="feature">
    <svg class="icon" width="52" height="52" viewBox="0 0 52 52"><circle cx="26" cy="26" r="25" fill="#222" stroke="#bbb"/><polygon points="26,17 37,33 15,33" fill="#ddd"/><polygon points="26,27 29,33 23,33" fill="#222"/></svg>
    <h2>Join Our<br>Bootcamp Now</h2>
    <p>Go for a week training &amp; refine your skills. We will train you, how to Get the woman of your Dreams</p>
  </article>
  <article class="feature">
    <svg class="icon" width="52" height="52" viewBox="0 0 52 52"><circle cx="26" cy="26" r="25" fill="#222" stroke="#bbb"/><text x="26" y="34" text-anchor="middle" font-family="Cabin,sans-serif" font-weight="500" font-size="24" fill="#eee">?</text></svg>
    <h2>Frequently Asked<br>Questions</h2>
    <p>Nulla vitae imperdiet elit. Quisque vehicula, nulla sit amet ultrices molestie, purus tortor consequat magna, et eleifend elit quam</p>
  </article>
</section>

<h2 class="stories-title">Success Stories</h2>
<blockquote class="quote">
  “Praesent sed magna augue, at pulvinar lorem. Ut vulputate mauris ac velit fermentum condimentum. Curabitur vel justo tellus, ut blandit erat. Vestibulum ante ipsum primis in faucibus orci luctus et ultrices posuere cubilia Curae; Aenean libero massa, lacinia elementum pulvinar et, fermentum in odio. Quisque eleifend quam acopi”
  <cite>Mark Dalton</cite>
</blockquote>

<div class="presenter" role="img" aria-label="Video presenter, a woman in a grey blazer standing with hands clasped"></div>

<svg class="edge edge-footer" viewBox="0 0 1200 5" preserveAspectRatio="none">
  <defs><pattern id="teeth-up" width="8" height="5" patternUnits="userSpaceOnUse"><path d="M0 5 L4 0 L8 5Z" fill="#d90000"/></pattern></defs>
  <rect width="1200" height="5" fill="url(#teeth-up)"/>
</svg>
<footer class="site-footer">
  <nav class="footer-nav">
    <a href="#">Home</a><a href="#">About us</a><a href="#">Bootcamp</a><a href="#">Learning Program</a><a href="#">FAQ</a><a href="#">Success Stories</a><a href="#">Contact us</a>
  </nav>
  <p class="copyright">Copyright © 2013 cordialkeys.com.au. All rights reserved</p>
  <div class="social"><span></span><span></span><span></span></div>
</footer>
</body>
</html>
```